New Webpage for High Class Expert Witness Services Company

We are looking for a minimalist design for a webpage that just has our logo and an entry form offer to connect with one of our Liaisons.
The entry form should just ask for Name, Email, Contact Info and Description of Project.

Company Name is: The Marlowe Crest Defense Services

Number of Pages Required

1 page

```html
<!DOCTYPE html>
<html lang="en">
<head>
<meta charset="utf-8">
<title>Marlowe Crest Defense Services — Connect with a Liaison</title>
<link rel="stylesheet" href="https://fonts.googleapis.com/css2?family=Crimson+Pro:wght@400;500&display=swap">
<style>
  :root {
    --page-bg: #121212;
    --text-light: #f2f2f2;
    --label-grey: #a9a9a9;
    --field-bg: #2a2a2a;
    --field-border: #5a5a5a;
    --button-top: #ffffff;
    --button-bottom: #a8a8a8;
    --button-text: #1c1c1c;
    --photo-light: #b9c4c8;
    --photo-dark: #1f2633;
  }
  * { box-sizing: border-box; margin: 0; padding: 0; }
  html, body {
    width: 1200px; height: 675px; overflow: hidden;
    background: var(--page-bg);
    font-family: "Crimson Pro", Georgia, serif;
    color: var(--text-light);
  }
  .page { position: relative; width: 1200px; height: 675px; }

  .brand {
    position: absolute; left: 98px; top: 28px;
    display: flex; align-items: center; gap: 10px;
    color: var(--text-light);
  }
  .brand-mark { width: 14px; height: 14px; background: var(--text-light); }
  .brand-name { font-size: 21px; font-weight: 400; line-height: 26px; }

  .menu-toggle { position: absolute; left: 1067px; top: 29px; }

  .liaison-photo {
    position: absolute; left: 92px; top: 84px;
    width: 460px; height: 529px; border-radius: 11px;
    background: linear-gradient(110deg, var(--photo-light) 0%, #8f9aa0 35%, var(--photo-dark) 60%, #5b4a3a 100%);
  }

  .hero-title {
    position: absolute; left: 597px; top: 106px;
    font-size: 51px; font-weight: 400; line-height: 59px;
    letter-spacing: -0.3px; white-space: nowrap;
  }

  .contact-form { position: absolute; left: 597px; top: 244px; width: 501px; }
  .form-row { display: flex; gap: 6px; }
  .form-field { flex: 1; display: flex; flex-direction: column; }
  .form-field label {
    font-size: 13px; color: var(--label-grey); height: 26px; line-height: 20px;
  }
  .form-field input, .form-field textarea {
    width: 100%; height: 40px; margin-bottom: 4px;
    background: var(--field-bg); border: 1px solid var(--field-border);
    border-radius: 5px; color: var(--text-light); font: inherit; resize: none;
  }
  .form-field textarea { height: 106px; }
  .submit-button {
    margin-top: 16px; width: 500px; height: 40px; border: none; border-radius: 5px;
    background: linear-gradient(180deg, var(--button-top), var(--button-bottom));
    color: var(--button-text); font-family: "Crimson Pro", Georgia, serif;
    font-size: 16px; letter-spacing: 0.5px;
  }
</style>
</head>
<body>
<main class="page">
  <header>
    <div class="brand">
      <span class="brand-mark" aria-hidden="true"></span>
      <span class="brand-name">The Marlowe Crest Defense Services</span>
    </div>
    <svg class="menu-toggle" width="36" height="27" viewBox="0 0 36 27" aria-label="Menu">
      <rect x="0" y="0" width="35" height="2" fill="#f2f2f2"/>
      <rect x="0" y="12" width="35" height="2" fill="#f2f2f2"/>
      <rect x="0" y="24" width="35" height="2" fill="#f2f2f2"/>
    </svg>
  </header>

  <div class="liaison-photo" role="img" aria-label="Photo of a liaison in a suit wearing a headset at a call-centre desk, colleagues behind"></div>

  <h1 class="hero-title">FOCUSED PROTECTION.<br>TRUSTED EXPERTISE.</h1>

  <form class="contact-form">
    <div class="form-row">
      <div class="form-field"><label for="first-name">First Name</label><input id="first-name" type="text"></div>
      <div class="form-field"><label for="last-name">Last Name</label><input id="last-name" type="text"></div>
    </div>
    <div class="form-row">
      <div class="form-field"><label for="email">Email</label><input id="email" type="email"></div>
      <div class="form-field"><label for="contact-info">Contact Info</label><input id="contact-info" type="text"></div>
    </div>
    <div class="form-row">
      <div class="form-field"><label for="project-description">Description of Project</label><textarea id="project-description"></textarea></div>
    </div>
    <button class="submit-button" type="submit">SUBMIT</button>
  </form>
</main>
</body>
</html>
```